Business Card for new Architectural Firm

I intend to practice in a rural mountain community in upstate NY, focusing on residential and light commercial projects, including second home / vacation properties. I wish to convey a feeling of rural outdoorsy modernity.

Color is important - bold and urbane. Secondary or tertiary colors preferred.

Font is important, idiosyncratic is ok

Optionally, I may choose to use the name Brackenfold Studio. If used as part of your design, all of the Must Haves are still required.

Images uploaded are logos I like

Industry/Entity Type

Residential

Contact Information for Business Card

Lionel Harwicke
Architect (This word should stand alone or be associated with my name - not license number)
NY License No. 052816
lionel@designlhq.com
607 382 9154

Font styles to use
Sans Serif
Decorative

Requirements
Must have
• Whatever files I need to best utilize your design
• PDF
• JPG
• EPS
• Vectorwhatsit
Nice to have
• Logo or element that can be incorporated into other print material.
• Could be a font based card
Should not have
• no clip art
• No templates
• no floor plans
• no building photographs

```html
<!DOCTYPE html>
<html lang="en">
<head>
<meta charset="utf-8">
<title>Lionel Harwicke, Architect: Business Card Options</title>
<link href="https://fonts.googleapis.com/css2?family=Advent+Pro:wght@300;400&family=Oswald:wght@500;600&family=Economica:wght@400&display=swap" rel="stylesheet">
<style>
  :root {
    --sheet: #ffffff;
    --card: #454545;
    --name: #dcdcdc;
    --accent: #8ed996;
    --detail: #ffffff;
    --art-light: #b9e3bc;
    --art-mid: #8ed996;
    --art-deep: #6abf78;
  }
  * { margin: 0; padding: 0; box-sizing: border-box; }
  html, body {
    width: 686px;
    height: 1200px;
    overflow: hidden;
    background: var(--sheet);
  }
  .sheet {
    width: 686px;
    height: 1200px;
    display: flex;
    flex-direction: column;
    justify-content: space-between;
  }
  .card {
    position: relative;
    width: 686px;
    height: 392px;
    background: var(--card);
    overflow: hidden;
  }
  .card__art {
    position: absolute;
    left: 300px;
    top: 71px;
    width: 386px;
    height: 321px;
    background: linear-gradient(120deg, var(--art-light) 0%, var(--art-mid) 45%, var(--art-deep) 100%);
  }
  .card__name {
    position: absolute;
    left: 24px;
    top: 14px;
    color: var(--name);
    font-size: 50px;
    line-height: 1.1;
    white-space: nowrap;
  }
  .card__title {
    position: absolute;
    left: 26px;
    top: 86px;
    color: var(--accent);
    font-size: 30px;
    line-height: 1.1;
  }
  .card__rule {
    position: absolute;
    left: 0;
    top: 240px;
    width: 276px;
    height: 3px;
    background: var(--accent);
  }
  .card__details {
    position: absolute;
    left: 26px;
    top: 254px;
    list-style: none;
    color: var(--detail);
    font-size: 27px;
    line-height: 43px;
    white-space: nowrap;
  }

  .card--light { font-family: "Advent Pro", sans-serif; }
  .card--light .card__name { font-weight: 300; }
  .card--light .card__title,
  .card--light .card__details { font-weight: 400; }

  .card--bold { font-family: "Oswald", sans-serif; }
  .card--bold .card__name { font-weight: 600; font-size: 50px; top: 8px; }
  .card--bold .card__title { font-weight: 500; font-size: 27px; top: 88px; }
  .card--bold .card__details { font-weight: 500; font-size: 24px; }

  .card--narrow { font-family: "Economica", sans-serif; }
  .card--narrow .card__name { font-size: 49px; letter-spacing: 1px; }
  .card--narrow .card__title { font-size: 27px; }
  .card--narrow .card__details { font-size: 26px; }
</style>
</head>
<body>
<main class="sheet">

  <section class="card card--light">
    <div class="card__art" role="img" aria-label="Layered green mountain-peak graphic"></div>
    <h1 class="card__name">Lionel Harwicke</h1>
    <p class="card__title">Architect</p>
    <div class="card__rule"></div>
    <ul class="card__details">
      <li>NY License No. 052816</li>
      <li>lionel@designlhq.com</li>
      <li>607. 382. 9154</li>
    </ul>
  </section>

  <section class="card card--bold">
    <div class="card__art" role="img" aria-label="Layered green mountain-peak graphic"></div>
    <h2 class="card__name">Lionel Harwicke</h2>
    <p class="card__title">Architect</p>
    <div class="card__rule"></div>
    <ul class="card__details">
      <li>NY License No. 052816</li>
      <li>lionel@designlhq.com</li>
      <li>607. 382. 9154</li>
    </ul>
  </section>

  <section class="card card--narrow">
    <div class="card__art" role="img" aria-label="Layered green mountain-peak graphic"></div>
    <h2 class="card__name">Lionel&nbsp; Harwicke</h2>
    <p class="card__title">Architect</p>
    <div class="card__rule"></div>
    <ul class="card__details">
      <li>NY License No. 052816</li>
      <li>lionel@designlhq.com</li>
      <li>607. 382. 9154</li>
    </ul>
  </section>

</main>
</body>
</html>
```